New Web Design Project for kitchen company

We need a homepage mockup for a company that sells and installs kitchen and baths. Use your creative talent to come up with something visually appeal and professional for this web-site.

Please see the attached brief.

If you have any questions feel free to post them right on the project discussion.

Target Market(s)

homeowners

Number of Pages Required

1 page

Font styles to use
Serif
Other font styles liked:
• Something similar to the logo

```html
<!DOCTYPE html>
<html lang="en">
<head>
<meta charset="utf-8">
<title>Harborline Kitchen and Bath</title>
<link href="https://fonts.googleapis.com/css2?family=Oswald:wght@300;400;500;600;700&family=Roboto:wght@400;500;700&family=Montserrat:wght@700&display=swap" rel="stylesheet">
<style>
:root{
  --orange:#f4732f;
  --ink:#1d1d1d;
  --text:#6f6f6f;
  --light:#f4f4f4;
  --white:#ffffff;
  --footer:#151515;
}
*{margin:0;padding:0;box-sizing:border-box}
html,body{width:1200px;height:3475px;overflow:hidden;background:var(--white)}
body{position:relative;font-family:'Roboto',Arial,sans-serif;color:var(--ink)}
.abs{position:absolute}
.head{font-family:'Oswald','Arial Narrow',sans-serif;font-weight:500;color:var(--ink)}
.para{font-size:13px;line-height:24px;color:var(--text)}

/* hero */
.hero-shape{left:0;top:0}
.logo{left:158px;top:42px;display:flex;align-items:center;gap:9px;color:var(--white)}
.logo-mark{width:44px;height:44px;border:2px solid var(--white);border-radius:50%}
.logo-name{font-family:'Oswald',sans-serif;font-weight:400;font-size:19px;letter-spacing:.5px;line-height:1}
.nav{top:56px;font-size:12px;font-weight:700;color:var(--white);letter-spacing:.2px}
.nav-active::after{content:"";position:absolute;left:4px;top:20px;width:10px;height:3px;background:var(--orange)}
.btn-outline{left:847px;top:45px;width:195px;height:37px;border:1.5px solid var(--white);border-radius:19px;color:var(--white);font-size:12px;font-weight:700;display:flex;align-items:center;justify-content:center}
.hero-welcome{left:0;width:1200px;top:200px;text-align:center;font-family:'Oswald',sans-serif;font-weight:300;font-size:31px;color:var(--white)}
.hero-title{left:0;width:1200px;top:244px;text-align:center;font-family:'Oswald',sans-serif;font-weight:600;font-size:42px;color:var(--white);letter-spacing:.5px}
.btn-orange{background:var(--orange);color:var(--white);font-family:'Oswald',sans-serif;font-weight:500;font-size:14px;display:flex;align-items:center;justify-content:center}
.hero-btn{left:523px;top:324px;width:154px;height:41px}
.dot{left:1033px;width:9px;height:9px;border:1px solid var(--white);border-radius:50%}

/* photo areas */
.photo-kitchen-card{background:
  linear-gradient(180deg,rgba(0,0,0,0) 55%,rgba(20,18,16,.85) 100%),
  radial-gradient(ellipse 30% 35% at 78% 32%,#efe9dc 0%,rgba(239,233,220,0) 100%),
  radial-gradient(ellipse 40% 30% at 40% 70%,#3a2a20 0%,rgba(58,42,32,0) 100%),
  linear-gradient(90deg,#6f6e6c 0%,#d8d3c8 35%,#b9ab97 60%,#e6e1d8 100%)}
.photo-bath-card{background:
  linear-gradient(180deg,rgba(0,0,0,0) 55%,rgba(25,22,18,.85) 100%),
  radial-gradient(ellipse 35% 45% at 65% 40%,#e8ddb6 0%,rgba(232,221,182,0) 100%),
  linear-gradient(90deg,#bfb48f 0%,#d9cfa8 30%,#a99a70 65%,#6e6450 100%)}
.card{overflow:hidden}
.card-label{left:90px;bottom:24px;font-family:'Oswald',sans-serif;font-weight:500;font-size:19px;color:var(--white)}
.card-icon{left:26px;bottom:20px}
.about-photo{background:
  radial-gradient(ellipse 18% 30% at 40% 20%,#f7f8f8 0%,rgba(247,248,248,0) 100%),
  radial-gradient(ellipse 30% 25% at 20% 80%,#e9e9e7 0%,rgba(233,233,231,0) 100%),
  radial-gradient(ellipse 12% 14% at 22% 70%,#d69a2c 0%,rgba(214,154,44,0) 100%),
  linear-gradient(180deg,rgba(0,0,0,0) 75%,rgba(40,60,110,.35) 100%),
  linear-gradient(90deg,#cfd4d7 0%,#a7acb0 30%,#8c8f91 50%,#4b4a48 75%,#5c5753 100%)}
.about-panel{left:604px;top:1026px;width:451px;height:377px;background:rgba(20,20,20,.9);border-radius:6px}
.btn-white{left:647px;top:1306px;width:151px;height:47px;background:var(--white);color:var(--ink);font-family:'Montserrat','Roboto',sans-serif;font-weight:700;font-size:14px;display:flex;align-items:center;justify-content:center}
.arrow{width:18px;height:18px;border-radius:50%;display:flex;align-items:center;justify-content:center}
.arrow-fill{background:var(--orange)}
.arrow-line{border:1px solid #555}
.ba-frame{border:4px solid var(--ink);display:flex;overflow:hidden}
.ba-frame div{flex:1}
.review{width:280px;height:206px;background:var(--white);box-shadow:0 2px 12px rgba(0,0,0,.1);padding:26px 20px}
.review-name{font-size:15px;font-weight:500;color:var(--ink)}
.review-role{font-size:11px;color:#999;margin-top:6px}
.review-text{font-size:12px;line-height:21px;color:var(--text);margin-top:20px}
.avatar{right:20px;top:22px;width:44px;height:44px;border-radius:50%;background:radial-gradient(circle at 50% 40%,#c9b3a1 0%,#8a7a6d 55%,#4b4744 100%)}

/* footer */
.foot-head{font-family:'Oswald',sans-serif;font-weight:500;font-size:18px;line-height:28px;color:var(--white)}
.foot-text{font-size:13px;color:#d6d6d6}
.field{left:487px;width:196px;border:1px solid #666;font-size:11px;color:#777;padding:10px 12px}
.links a{display:block;color:#d6d6d6;text-decoration:none;font-size:13px;height:29px}
.social{top:3383px;width:18px;height:18px;border-radius:50%}
</style>
</head>
<body>

<!-- HERO -->
<svg class="abs hero-shape" width="1200" height="560" viewBox="0 0 1200 560" role="img" aria-label="Photo of a finished open-plan kitchen with dark island, windows and hardwood floor">
  <defs>
    <clipPath id="heroClip"><path d="M0 0H1200V505Q1198 548 1145 552L115 475Q62 468 52 418L0 140Z"/></clipPath>
    <linearGradient id="heroBase" x1="0" y1="0" x2="1" y2="0">
      <stop offset="0" stop-color="#5d6573"/>
      <stop offset=".35" stop-color="#4a5466"/>
      <stop offset=".65" stop-color="#3a4252"/>
      <stop offset="1" stop-color="#5a6070"/>
    </linearGradient>
    <radialGradient id="heroWindow" cx=".55" cy=".2" r=".35">
      <stop offset="0" stop-color="#b9c2cf" stop-opacity=".9"/>
      <stop offset="1" stop-color="#b9c2cf" stop-opacity="0"/>
    </radialGradient>
    <radialGradient id="heroGreen" cx=".08" cy=".42" r=".12">
      <stop offset="0" stop-color="#4d6a3c" stop-opacity=".8"/>
      <stop offset="1" stop-color="#4d6a3c" stop-opacity="0"/>
    </radialGradient>
    <linearGradient id="heroFloor" x1="0" y1="0" x2="0" y2="1">
      <stop offset=".55" stop-color="#1c1a20" stop-opacity="0"/>
      <stop offset="1" stop-color="#1c1a20" stop-opacity=".85"/>
    </linearGradient>
    <linearGradient id="heroShade" x1="0" y1="0" x2="0" y2="1">
      <stop offset="0" stop-color="#101522" stop-opacity=".35"/>
      <stop offset="1" stop-color="#101522" stop-opacity=".1"/>
    </linearGradient>
  </defs>
  <g clip-path="url(#heroClip)">
    <rect width="1200" height="560" fill="url(#heroBase)"/>
    <rect width="1200" height="560" fill="url(#heroWindow)"/>
    <rect width="1200" height="560" fill="url(#heroGreen)"/>
    <rect width="1200" height="560" fill="url(#heroFloor)"/>
    <rect width="1200" height="560" fill="url(#heroShade)"/>
  </g>
</svg>

<div class="abs logo"><span class="logo-mark"></span><span class="logo-name">HARBORLINE</span></div>
<div class="abs nav nav-active" style="left:397px">HOME</div>
<div class="abs nav" style="left:465px">ABOUT US</div>
<div class="abs nav" style="left:558px">SERVICES</div>
<div class="abs nav" style="left:652px">PROJECTS</div>
<div class="abs nav" style="left:748px">CONTACT US</div>
<div class="abs btn-outline">SCHEDULE INSTALLATION</div>

<div class="abs hero-welcome">Welcome to Harborline</div>
<div class="abs hero-title">KITCHEN &amp; BATH COMMITTED TO QUALITY</div>
<div class="abs btn-orange hero-btn">VIEW OUR SERVICES</div>

<svg class="abs" style="left:1031px;top:237px" width="14" height="8"><path d="M1 7L7 1L13 7" stroke="#fff" fill="none" stroke-width="1.3"/></svg>
<div class="abs dot" style="top:258px"></div>
<div class="abs dot" style="top:282px;background:var(--orange);border-color:var(--orange)"></div>
<div class="abs dot" style="top:306px"></div>
<div class="abs dot" style="top:330px"></div>
<svg class="abs" style="left:1031px;top:352px" width="14" height="8"><path d="M1 1L7 7L13 1" stroke="#fff" fill="none" stroke-width="1.3"/></svg>

<!-- SERVICES -->
<h2 class="abs head" style="left:158px;top:520px;font-size:29px">Our Services</h2>
<p class="abs para" style="left:160px;top:570px;width:400px">Lorem ipsum dolor sit amet, consectetuer adipiscing elit, sed diahun guo noipuna nonummy</p>

<div class="abs card photo-kitchen-card" style="left:158px;top:650px;width:430px;height:270px" role="img" aria-label="Photo of a white kitchen with island and pendant lights">
  <svg class="abs card-icon" width="50" height="40" viewBox="0 0 50 40" fill="none" stroke="#fff" stroke-width="2"><rect x="2" y="18" width="30" height="20"/><rect x="36" y="8" width="12" height="30"/><path d="M6 12h10M11 2v10M22 4l4 8M2 26h30"/></svg>
  <div class="abs card-label">Kitchen Installation</div>
</div>
<div class="abs card photo-bath-card" style="left:611px;top:650px;width:430px;height:270px" role="img" aria-label="Photo of a bathroom with tiled walk-in shower and freestanding tub">
  <svg class="abs card-icon" width="50" height="40" viewBox="0 0 50 40" fill="none" stroke="#fff" stroke-width="2"><path d="M2 20h46v6a10 10 0 0 1-10 10H12A10 10 0 0 1 2 26z"/><path d="M8 20V6a4 4 0 0 1 8 0M12 36l-2 4M38 36l2 4"/></svg>
  <div class="abs card-label">Bathroom Installation</div>
</div>

<!-- ABOUT -->
<div class="abs about-photo" style="left:0;top:979px;width:1200px;height:471px" role="img" aria-label="Photo of a bright kitchen with marble counters and a kettle on the stove"></div>
<div class="abs about-panel"></div>
<div class="abs" style="left:644px;top:1070px;font-family:'Oswald',sans-serif;font-weight:300;font-size:29px;color:var(--orange)">About</div>
<h2 class="abs head" style="left:644px;top:1115px;font-size:30px;line-height:39px;color:var(--white)">HARBORLINE KITCHEN<br>AND BATH INC</h2>
<p class="abs" style="left:644px;top:1208px;width:340px;font-size:13px;line-height:24px;color:#e6e6e6">Lorem ipsum dolor sit amet, consectetuer adipiscing elit, sed diahun guo noipuna nonummy nibh euismod tincidunt ut.Consectetuer adipiscing elit oremio ipsum.</p>
<div class="abs btn-white">KNOW MORE</div>

<!-- PROJECTS -->
<h2 class="abs head" style="left:154px;top:1508px;font-size:29px">Our Recent Projects</h2>
<p class="abs para" style="left:156px;top:1559px;width:420px">Lorem ipsum dolor sit amet, consectetuer adipiscing elit, sed diahun guo noipuna nonummy</p>
<div class="abs" style="left:158px;top:1630px;width:202px;height:195px;background:radial-gradient(ellipse 40% 35% at 35% 80%,#f2f1ee 0%,rgba(242,241,238,0) 100%),radial-gradient(ellipse 40% 40% at 70% 35%,#ddd3bd 0%,rgba(221,211,189,0) 100%),linear-gradient(90deg,#8d8474,#c9bea7 50%,#b3a68c)" role="img" aria-label="Photo of a bathroom with tub and glass shower"></div>
<div class="abs" style="left:383px;top:1630px;width:202px;height:195px;background:radial-gradient(ellipse 25% 30% at 62% 55%,#3e6e8e 0%,rgba(62,110,142,0) 100%),linear-gradient(180deg,rgba(0,0,0,0) 65%,#6a5a4a 100%),linear-gradient(90deg,#7f8a96,#d5dade 45%,#a9b1b9)" role="img" aria-label="Photo of a hallway leading to a dining room"></div>
<div class="abs" style="left:158px;top:1847px;width:202px;height:195px;background:linear-gradient(90deg,#2a2a2a 0%,#3c3c3c 30%,#e6e6e6 45%,#d0d0d0 55%,#222 70%,#1a1a1a 100%)" role="img" aria-label="Photo of a laundry closet with dark doors"></div>
<div class="abs" style="left:383px;top:1847px;width:202px;height:195px;background:radial-gradient(ellipse 30% 25% at 60% 75%,#4a3528 0%,rgba(74,53,40,0) 100%),linear-gradient(90deg,#9aa0a4,#e4e6e7 40%,#cfcfcb 70%,#8f8a80)" role="img" aria-label="Photo of a white kitchen with island"></div>
<div class="abs" style="left:615px;top:1521px;width:585px;height:521px;background:radial-gradient(ellipse 30% 20% at 45% 55%,#ece8e1 0%,rgba(236,232,225,0) 100%),radial-gradient(ellipse 25% 22% at 48% 73%,#4a4440 0%,rgba(74,68,64,0) 100%),radial-gradient(ellipse 18% 12% at 90% 92%,#7a1e1e 0%,rgba(122,30,30,0) 100%),linear-gradient(180deg,#e9e6e0 0%,#cfc8bd 35%,#8f8478 65%,#6b4a30 85%,#4a3322 100%)" role="img" aria-label="Photo of a large kitchen with grey island, pendant lights and hardwood floor"></div>
<div class="abs" style="left:779px;top:2042px;width:421px;height:10px;background:var(--orange)"></div>
<div class="abs arrow arrow-fill" style="left:100px;top:1813px"><svg width="8" height="6"><path d="M1 5L4 2L7 5" stroke="#fff" fill="none" stroke-width="1.3"/></svg></div>
<div class="abs arrow arrow-line" style="left:100px;top:1840px"><svg width="8" height="6"><path d="M1 1L4 4L7 1" stroke="#555" fill="none" stroke-width="1.3"/></svg></div>

<!-- BEFORE AFTER -->
<div class="abs" style="left:0;top:2116px;width:1200px;height:411px;background:var(--light)"></div>
<h2 class="abs head" style="left:0;width:1178px;text-align:center;top:2159px;font-size:29px">Before After</h2>
<div class="abs ba-frame" style="left:156px;top:2231px;width:430px;height:214px" role="img" aria-label="Before and after photos of a kitchen renovation">
  <div style="background:radial-gradient(ellipse 35% 30% at 50% 30%,#e6c48f 0%,rgba(230,196,143,0) 100%),radial-gradient(ellipse 40% 12% at 45% 78%,#d9a53a 0%,rgba(217,165,58,0) 100%),linear-gradient(180deg,#5a3a22,#2a1c14 70%,#3a2e28)"></div>
  <div style="background:radial-gradient(ellipse 30% 25% at 55% 70%,#2a2a2c 0%,rgba(42,42,44,0) 100%),linear-gradient(180deg,#f4f4f3,#dcdcda 60%,#9a948c)"></div>
</div>
<div class="abs ba-frame" style="left:611px;top:2231px;width:430px;height:214px" role="img" aria-label="Before and after photos of a bathroom renovation">
  <div style="background:radial-gradient(ellipse 30% 20% at 45% 70%,#e8e8e4 0%,rgba(232,232,228,0) 100%),linear-gradient(90deg,#4e5046,#6d6a52 50%,#5c5a46)"></div>
  <div style="background:radial-gradient(ellipse 14% 22% at 80% 45%,#e9b7c2 0%,rgba(233,183,194,0) 100%),radial-gradient(ellipse 40% 15% at 40% 70%,#2a2a2a 0%,rgba(42,42,42,0) 100%),linear-gradient(180deg,#f7f7f7,#e6e6e6 70%,#a4a4a4)"></div>
</div>
<div class="abs arrow arrow-line" style="left:100px;top:2343px"><svg width="6" height="8"><path d="M5 1L2 4L5 7" stroke="#555" fill="none" stroke-width="1.3"/></svg></div>
<div class="abs arrow arrow-fill" style="left:1076px;top:2317px"><svg width="6" height="8"><path d="M1 1L4 4L1 7" stroke="#fff" fill="none" stroke-width="1.3"/></svg></div>

<!-- TESTIMONIALS -->
<h2 class="abs head" style="left:0;width:1138px;text-align:center;top:2557px;font-size:29px">Our Customers Say</h2>
<div class="abs review" style="left:155px;top:2642px"><span class="abs avatar" role="img" aria-label="Customer portrait"></span><div class="review-name">Mara Venn</div><div class="review-role">Vise Business Analyst</div><p class="review-text">Lorem ipsum dolor sit amet, consectetur adipiscing elit, sed do eiusmod tempor incididunt ut labore et dolore magna aliqua. Ut enim ad</p></div>
<div class="abs review" style="left:460px;top:2642px"><span class="abs avatar" role="img" aria-label="Customer portrait"></span><div class="review-name">Mara Venn</div><div class="review-role">Vise Business Analyst</div><p class="review-text">Lorem ipsum dolor sit amet, consectetur adipiscing elit, sed do eiusmod tempor incididunt ut labore et dolore magna aliqua. Ut enim ad</p></div>
<div class="abs review" style="left:763px;top:2642px"><span class="abs avatar" role="img" aria-label="Customer portrait"></span><div class="review-name">Mara Venn</div><div class="review-role">Vise Business Analyst</div><p class="review-text">Lorem ipsum dolor sit amet, consectetur adipiscing elit, sed do eiusmod tempor incididunt ut labore et dolore magna aliqua. Ut enim ad</p></div>
<span class="abs" style="left:573px;top:2890px;width:6px;height:6px;border-radius:50%;background:#ccc"></span>
<span class="abs" style="left:597px;top:2890px;width:6px;height:6px;border-radius:50%;background:#e0a020"></span>
<span class="abs" style="left:621px;top:2890px;width:6px;height:6px;border-radius:50%;background:#ccc"></span>

<!-- FOOTER -->
<svg class="abs" style="left:0;top:2890px" width="1200" height="585" viewBox="0 0 1200 585" role="img" aria-label="Dimmed photo of a dark kitchen interior with pendant lights">
  <defs>
    <radialGradient id="footGlowA" cx=".12" cy=".35" r=".25"><stop offset="0" stop-color="#3a3836"/><stop offset="1" stop-color="#3a3836" stop-opacity="0"/></radialGradient>
    <radialGradient id="footGlowB" cx=".62" cy=".25" r=".2"><stop offset="0" stop-color="#33302c"/><stop offset="1" stop-color="#33302c" stop-opacity="0"/></radialGradient>
    <radialGradient id="footGlowC" cx=".92" cy=".6" r=".2"><stop offset="0" stop-color="#2c2a28"/><stop offset="1" stop-color="#2c2a28" stop-opacity="0"/></radialGradient>
    <clipPath id="footClip"><path d="M0 60Q10 10 70 12L1100 100Q1145 110 1158 160L1200 340V585H0Z"/></clipPath>
  </defs>
  <g clip-path="url(#footClip)">
    <rect width="1200" height="585" fill="var(--footer)"/>
    <rect width="1200" height="585" fill="url(#footGlowA)"/>
    <rect width="1200" height="585" fill="url(#footGlowB)"/>
    <rect width="1200" height="585" fill="url(#footGlowC)"/>
  </g>
</svg>
<div class="abs foot-head" style="left:156px;top:3040px">Do you have anyquestions<br>and want to contact us?</div>
<div class="abs" style="left:156px;top:3100px;font-family:'Oswald',sans-serif;font-weight:500;font-size:22px;color:var(--orange)">Call or Visit us</div>
<svg class="abs" style="left:158px;top:3160px" width="14" height="22" viewBox="0 0 14 22" fill="none" stroke="var(--orange)" stroke-width="1.5"><rect x="1" y="1" width="12" height="20" rx="2"/><path d="M5 17h4"/></svg>
<div class="abs" style="left:189px;top:3157px;font-family:'Oswald',sans-serif;font-weight:500;font-size:20px;color:var(--orange)">+1 - 555 0142 300</div>
<svg class="abs" style="left:158px;top:3222px" width="14" height="18" viewBox="0 0 14 18" fill="none" stroke="var(--orange)" stroke-width="1.5"><path d="M7 17S1 10 1 6.5a6 6 0 0 1 12 0C13 10 7 17 7 17z"/><circle cx="7" cy="6.5" r="2"/></svg>
<div class="abs foot-text" style="left:189px;top:3218px;line-height:28px">42 Example Lane,<br>Springfield, ST 00000, USA</div>
<svg class="abs" style="left:158px;top:3286px" width="16" height="12" viewBox="0 0 16 12" fill="none" stroke="var(--orange)" stroke-width="1.3"><rect x=".7" y=".7" width="14.6" height="10.6"/><path d="M1 1l7 6 7-6"/></svg>
<div class="abs foot-text" style="left:189px;top:3283px">hello@harborlinekb.com</div>

<div class="abs foot-head" style="left:481px;top:3040px">Do you want receive quote?</div>
<div class="abs field" style="top:3085px;height:36px">Name</div>
<div class="abs field" style="top:3131px;height:36px">Phone number</div>
<div class="abs field" style="top:3177px;height:36px">Email address</div>
<div class="abs field" style="top:3224px;height:56px">Message</div>
<div class="abs btn-orange" style="left:487px;top:3300px;width:196px;height:32px">SEND NOW</div>

<div class="abs foot-head" style="left:825px;top:3038px">Useful Links</div>
<nav class="abs links" style="left:827px;top:3081px"><a>Home</a><a>About us</a><a>Services</a><a>Portfolio</a><a>Contact us</a></nav>

<div class="abs" style="left:168px;top:3387px;font-size:10px;color:#555">@2020 HARBORLINE.com. All Rights Reserved</div>
<span class="abs social" style="left:885px;background:#3b5998"></span>
<span class="abs social" style="left:916px;background:#1da1f2"></span>
<span class="abs social" style="left:947px;background:#dd4b39"></span>
<span class="abs social" style="left:978px;background:#e52d27"></span>

</body>
</html>
```